Redesign Login page

I want to redesign my login page to bring my 2 products closer together. I am only looking to redesign one login page, not 2.

For the logo, please make it solid and it can be black or white if helpful. I can also fine tune the logo if you get it close.

Coding

Coded - Design and coding required

Number of Pages Required

1 page

```html
<!DOCTYPE html>
<html lang="en">
<head>
<meta charset="utf-8">
<title>Tarnview – Login</title>
<link href="https://fonts.googleapis.com/css2?family=Inter:wght@400;500;600&display=swap" rel="stylesheet">
<style>
  :root {
    --page-bg: #f5f7f6;
    --brand-dark: #012d2a;
    --brand-teal: #02524f;
    --panel: #ffffff;
    --field-bg: #f1f2f2;
    --ink: #111614;
    --ink-soft: #4a4f4d;
    --icon-grey: #b9bcbb;
    --line: #dcdfde;
    --link: #1f4d49;
    --sso-border: #c9cccb;
  }
  * { box-sizing: border-box; margin: 0; padding: 0; }
  html, body {
    width: 1200px; height: 800px; overflow: hidden;
    background: var(--page-bg);
    font-family: "Inter", Arial, sans-serif;
    color: var(--ink);
  }
  .login-card {
    position: absolute; left: 419px; top: 150px;
    width: 362px; height: 524px;
    border-radius: 31px;
    background: linear-gradient(115deg, var(--brand-dark) 0 52%, var(--brand-teal) 52% 100%);
    overflow: hidden;
  }
  .brand {
    position: absolute; left: 0; right: 0; top: 18px;
    text-align: center;
    font-size: 26px; font-weight: 600; letter-spacing: -0.5px;
    color: #ffffff;
  }
  .login-panel {
    position: absolute; left: 4px; right: 4px; top: 66px; bottom: 4px;
    background: var(--panel);
    border-radius: 27px;
  }
  .login-title {
    position: absolute; left: 0; right: 0; top: 42px;
    text-align: center; font-size: 16.5px; font-weight: 400; color: var(--brand-dark);
  }
  .field {
    position: absolute; left: 27px; width: 300px; height: 44px;
    background: var(--field-bg); border-radius: 14px;
  }
  .field-email { top: 75px; }
  .field-password { top: 126px; }
  .field svg.lead { position: absolute; left: 16px; top: 14px; }
  .field-label {
    position: absolute; left: 41px; top: 11px; font-size: 12.5px; color: var(--ink);
  }
  .field-hint {
    position: absolute; left: 41px; top: 25px; font-size: 9.5px; color: var(--ink-soft);
  }
  .field .toggle { position: absolute; right: 14px; top: 14px; }
  .continue-btn {
    position: absolute; left: 27px; top: 176px; width: 300px; height: 44px;
    background: var(--brand-dark); border-radius: 22px;
    color: #fff; font-size: 12.5px; font-weight: 500;
    display: flex; align-items: center; justify-content: center;
  }
  .continue-btn svg { position: absolute; right: 18px; top: 17px; }
  .options-row {
    position: absolute; left: 29px; width: 298px; top: 230px;
    display: flex; justify-content: space-between; align-items: center;
    font-size: 12.5px;
  }
  .remember { display: flex; align-items: center; gap: 9px; }
  .checkbox {
    width: 16px; height: 16px; border: 1px solid #a9adab; border-radius: 4px; background: #fff;
  }
  .text-link { color: var(--link); text-decoration: underline; text-underline-offset: 2px; }
  .forgot { color: var(--brand-dark); }
  .signup-line {
    position: absolute; left: 0; right: 0; top: 267px;
    text-align: center; font-size: 12.5px;
  }
  .divider {
    position: absolute; left: 27px; width: 300px; top: 306px; height: 1px; background: var(--line);
  }
  .divider-badge {
    position: absolute; left: 161px; top: 292px; width: 29px; height: 29px;
    border: 1px solid #c3c6c5; border-radius: 50%; background: #fff;
    font-size: 9px; display: flex; align-items: center; justify-content: center;
  }
  .sso-btn {
    position: absolute; left: 27px; width: 300px; height: 45px;
    border: 1px solid var(--sso-border); border-radius: 12px; background: #fff;
    display: flex; align-items: center; justify-content: center; gap: 10px;
    font-size: 12.5px;
  }
  .sso-orbit { top: 332px; }
  .sso-quadra { top: 382px; }
  .sso-mark { width: 15px; height: 15px; background: var(--brand-teal); }
  .sso-mark.round { border-radius: 50%; }
</style>
</head>
<body>
  <main class="login-card">
    <div class="brand">Tarnview</div>

    <section class="login-panel">
      <h1 class="login-title">Login to Your Account</h1>

      <div class="field field-email">
        <svg class="lead" width="14" height="14" viewBox="0 0 14 14">
          <rect x="0.5" y="2.5" width="13" height="9" rx="1" fill="var(--icon-grey)"/>
          <path d="M1 3.5 L7 8 L13 3.5" fill="none" stroke="#fff" stroke-width="1.2"/>
        </svg>
        <span class="field-label">Email</span>
        <span class="field-hint">Enter your email</span>
      </div>

      <div class="field field-password">
        <svg class="lead" width="14" height="16" viewBox="0 0 14 16">
          <path d="M4 7 V4.5 a3 3 0 0 1 6 0" fill="none" stroke="var(--icon-grey)" stroke-width="1.4"/>
          <rect x="2.5" y="7" width="9" height="8" rx="2" fill="var(--icon-grey)"/>
          <circle cx="7" cy="11" r="1.2" fill="#fff"/>
        </svg>
        <span class="field-label">Password</span>
        <span class="field-hint">**************</span>
        <svg class="toggle" width="22" height="16" viewBox="0 0 22 16">
          <path d="M1.5 8 C5 2.5 17 2.5 20.5 8 C17 13.5 5 13.5 1.5 8 Z" fill="none" stroke="var(--icon-grey)" stroke-width="1.8"/>
          <circle cx="11" cy="8" r="2.8" fill="var(--icon-grey)"/>
          <line x1="4" y1="1.5" x2="18" y2="14.5" stroke="var(--icon-grey)" stroke-width="1.8"/>
        </svg>
      </div>

      <div class="continue-btn">Continue
        <svg width="12" height="10" viewBox="0 0 12 10">
          <path d="M0.5 5 H11 M7 1 L11 5 L7 9" fill="none" stroke="#fff" stroke-width="1.1"/>
        </svg>
      </div>

      <div class="options-row">
        <label class="remember"><span class="checkbox"></span>Remember me</label>
        <span class="text-link forgot">Forgot Password?</span>
      </div>

      <p class="signup-line">Don't have an account? <span class="text-link">Sign up</span></p>

      <div class="divider"></div>
      <div class="divider-badge">OR</div>

      <div class="sso-btn sso-orbit"><span class="sso-mark round"></span>Orbit SSO</div>
      <div class="sso-btn sso-quadra"><span class="sso-mark"></span>Quadra SSO</div>
    </section>
  </main>
</body>
</html>
```